BRINDLEWOOD MEDICAL SERVICES , stationary design

Clean , minimal , modern

Target Market(s)

Healthcare

Font styles to use
Sans Serif
Other font styles liked:
• Sans serif rounded light

Colors
b1b1b1

Requirements
Must have
• Must Have:
• - must have letter head, business card, envelope, fax sheet, id badge, folder, thank you card, notebook, invoice sheet, stamp , received stamp
• Nice to Have:
• - nice to have them all custom made (letterhead,envelope, business card, I’d badge etc
• - you need to change the logo colors , icon to dark blue and logo text to dark grey and another option with dark green icon and dark grey logo text .

```html
<!DOCTYPE html>
<html lang="en">
<head>
<meta charset="utf-8">
<title>Brindlewood Medical Services – Stationery Set</title>
<link href="https://fonts.googleapis.com/css2?family=Montserrat:wght@400;600;700;800&family=Courier+Prime&display=swap" rel="stylesheet">
<style>
  :root{
    --canvas:#e8e9eb;
    --paper:#ffffff;
    --navy:#1c2a63;
    --blue:#0c4da6;
    --grey:#b1b1b1;
    --grey-dark:#9d9d9d;
    --ink:#555a63;
    --line:#c9c9c9;
  }
  *{box-sizing:border-box;margin:0;padding:0}
  html,body{width:1200px;height:1200px;overflow:hidden}
  body{background:var(--canvas);position:relative;font-family:"Montserrat",sans-serif;color:var(--ink)}
  .item{position:absolute;background:var(--paper)}
  .accent{position:absolute;left:0;right:0;bottom:0;height:3px;background:linear-gradient(90deg,var(--navy) 0 32%,var(--grey) 32% 100%)}
  .brand{display:flex;align-items:center;gap:4px;font-family:"Montserrat",sans-serif;font-weight:700;color:var(--navy);white-space:nowrap;line-height:1}
  .brand .mark{display:inline-block;width:.9em;height:.9em;border:1.5px solid currentColor}
  .brand.light{color:#fff}
  .mono{font-family:"Courier Prime",monospace;color:#666;font-size:3.6px;line-height:1.45}
  .pattern{background:linear-gradient(135deg,#b4b4b4,#a6a6a6)}
  .contact{list-style:none;font-size:3px;color:#fff;line-height:1.7}
  .contact li::before{content:"";display:inline-block;width:3px;height:3px;margin-right:3px;background:currentColor;border-radius:50%;vertical-align:middle}

  /* Folder */
  .folder-shape{position:absolute;left:110px;top:70px}
  .folder-pocket-brand{position:absolute;left:174px;top:325px;font-size:8px}
  .folder-contact{position:absolute;left:174px;top:347px}
  .folder-cover{left:378px;top:70px;width:224px;height:308px}
  .folder-cover .brand{position:absolute;left:50%;top:160px;transform:translateX(-50%);font-size:15px;flex-direction:column;gap:6px}

  /* Letterhead */
  .letterhead{left:656px;top:70px;width:218px;height:308px;padding:36px 24px 0}
  .letterhead .brand{font-size:8px;margin-bottom:32px}
  .lh-meta{display:flex;justify-content:space-between;margin-bottom:10px}
  .lh-meta span{font-size:3.6px}
  .letterhead p{margin-bottom:6px}
  .signoff{position:absolute;right:24px;top:200px;text-align:center;font-size:4px;color:#777}
  .signoff .sig-line{width:40px;border-bottom:.6px solid #999;margin:0 auto 3px;height:12px}
  .lh-contact{position:absolute;left:24px;bottom:30px}
  .lh-contact .contact{color:#666;font-size:2.8px}

  /* Business card */
  .card-front{left:920px;top:153px;width:138px;height:80px;padding:14px 10px}
  .card-front .brand{font-size:6px}
  .card-name{position:absolute;right:10px;top:14px;text-align:right;font-size:4px;font-weight:600;color:var(--navy)}
  .card-name small{display:block;font-size:2.6px;font-weight:400;color:#777}
  .card-front .contact{color:#666;font-size:2.6px;margin-top:14px}
  .card-back{left:921px;top:247px;width:137px;height:79px}
  .card-back .brand{position:absolute;left:50%;top:50%;transform:translate(-50%,-50%);font-size:8px}

  /* Fax & Invoice */
  .sheet{width:219px;height:308px}
  .fax{left:91px;top:502px}
  .fax .brand{position:absolute;right:22px;top:38px;font-size:12px}
  .sheet-title{font-weight:700;color:var(--blue)}
  .fax .sheet-title{position:absolute;right:22px;top:66px;font-size:6.5px}
  .fax-fields{position:absolute;left:22px;top:96px;width:176px;display:grid;grid-template-columns:1fr 1fr;column-gap:6px;font-size:3.6px;font-family:"Courier Prime",monospace;color:#555;line-height:2.7}
  .fax-rule{position:absolute;left:22px;right:22px;top:153px;border-top:.6px solid #999}
  .fax-body{position:absolute;left:22px;right:22px;top:165px}

  .invoice{left:334px;top:502px}
  .invoice .brand{position:absolute;left:50%;top:34px;transform:translateX(-50%);font-size:9px}
  .invoice .sheet-title{position:absolute;left:0;right:0;top:66px;text-align:center;font-size:11px}
  .inv-head{position:absolute;left:28px;right:28px;top:98px;display:flex;justify-content:space-between}
  .inv-table{position:absolute;left:28px;top:122px;width:164px;border-collapse:collapse;font-family:"Courier Prime",monospace;font-size:3.4px;color:#333}
  .inv-table th{background:var(--blue);color:#fff;font-weight:400;padding:1.5px 3px;text-align:left}
  .inv-table td{border:.7px solid #222;padding:2.6px 3px}
  .inv-table .num{text-align:right}
  .inv-totals{position:absolute;right:28px;top:190px;text-align:right}
  .inv-total{position:absolute;right:28px;top:210px;font-family:"Courier Prime",monospace;font-size:4.6px;color:#222;font-weight:700}
  .inv-notes{position:absolute;left:28px;top:190px}
  .inv-thanks{position:absolute;left:28px;top:236px}
  .inv-sign{position:absolute;right:28px;top:244px;width:44px;border-bottom:.7px solid var(--navy)}

  /* ID badge */
  .badge{width:138px}
  .badge .slot{position:absolute;left:50%;top:12px;transform:translateX(-50%);width:34px;height:4px;border-radius:2px;background:#d4d4d4}
  .badge-front{left:613px;top:432px;height:204px}
  .badge-photo{position:absolute;left:50%;top:36px;transform:translateX(-50%);width:84px;height:84px;border-radius:50%;border:3px solid var(--navy);background:linear-gradient(180deg,#dfe4ea,#f5f6f7)}
  .badge-name{position:absolute;left:0;right:0;top:135px;text-align:center;font-size:6.5px;font-weight:700;color:#222}
  .badge-name small{display:block;font-size:3.5px;color:var(--blue);font-weight:600}
  .badge-front .brand{position:absolute;left:50%;top:160px;transform:translateX(-50%);font-size:9px}
  .badge-back{left:615px;top:654px;height:204px}
  .badge-info{position:absolute;left:13px;right:8px;top:44px;display:grid;grid-template-columns:62px 8px 1fr;font-size:5px;color:#666;row-gap:8px}
  .badge-back .brand{position:absolute;left:50%;top:150px;transform:translateX(-50%);font-size:7.5px}
  .badge-url{position:absolute;left:0;right:0;top:178px;text-align:center;font-size:4.6px;color:#555}

  /* Thank you card */
  .thanks{left:808px;top:444px;width:289px;height:206px}
  .thanks-word{position:absolute;font-weight:800;color:var(--blue);line-height:1}
  .thanks .w1{left:20px;top:48px;font-size:42px}
  .thanks .w2{left:195px;top:70px;font-size:42px}
  .thanks-copy{position:absolute;left:21px;top:94px;font-size:6.2px;color:#555;line-height:1.35}
  .stetho{position:absolute;left:156px;top:64px;width:38px;height:110px;border-radius:19px;background:linear-gradient(180deg,#e9eaec,#d3d5d8)}
  .thanks .brand{position:absolute;left:20px;top:176px;font-size:9px}

  /* Envelope */
  .env-back{left:106px;top:886px;width:348px;height:176px}
  .env-flap{position:absolute;left:0;top:0;width:100%;height:58px;clip-path:polygon(0 0,100% 0,98% 100%,2% 100%)}
  .env-back .brand{position:absolute;left:50%;top:26px;transform:translateX(-50%);font-size:11px}
  .env-front{left:212px;top:963px;width:347px;height:174px;border-top:3px solid var(--grey)}
  .env-front .brand{position:absolute;left:30px;top:58px;font-size:11px}
  .env-contact{position:absolute;left:28px;top:106px}
  .env-contact .contact{color:#555;font-size:4.6px}
  .env-window{position:absolute;left:210px;top:86px;width:112px;height:52px;border-radius:9px;background:linear-gradient(135deg,#22347a,#1b2a63)}

  /* Stamp impression */
  .stamp{left:625px;top:930px;width:251px;height:188px;clip-path:polygon(12% 0,100% 0,100% 40%,82% 100%,0 100%,0 30%)}
  .stamp .brand{position:absolute;left:118px;top:100px;font-size:10px;color:#9b9b9b;transform:rotate(18deg);transform-origin:left center}

  /* Notebook */
  .notebook{left:909px;top:743px;width:225px;height:319px;border-radius:9px}
  .notebook .brand{position:absolute;left:126px;top:250px;font-size:8px}
  .notebook-contact{position:absolute;left:126px;top:272px}
  .rings{position:absolute;left:898px;top:757px;width:24px}
  .rings span{display:block;height:5px;margin-bottom:16.2px;border-radius:3px;background:var(--navy)}
</style>
</head>
<body>

<!-- Folder -->
<svg class="folder-shape" width="268" height="362" viewBox="0 0 268 362" role="img" aria-label="Folder pocket with hexagon pattern">
  <polygon points="44,0 268,0 268,310 233,310 216,362 44,362 44,300 0,260 0,20" fill="#ababab"/>
  <polygon points="44,0 0,20 0,260 44,300" fill="#bdbdbd"/>
</svg>
<div class="brand light folder-pocket-brand"><span class="mark"></span>brindlewood medical services</div>
<ul class="contact folder-contact">
  <li>Phone : (+012) 555 014 2</li>
  <li>Email : info@brindlewoodmedical.com</li>
  <li>Web : www.brindlewoodmedical.com</li>
  <li>Address : 18 Harrow Lane, Millbrook, NJ 07999</li>
</ul>
<section class="item folder-cover">
  <div class="brand"><span class="mark"></span>brindlewood medical services</div>
</section>

<!-- Letterhead -->
<section class="item letterhead">
  <div class="brand"><span class="mark"></span>brindlewood medical services</div>
  <div class="lh-meta mono"><span>Dear, Mr ________</span><span>Date : ________</span></div>
  <p class="mono">We write to confirm your appointment details and the care plan agreed with our team. Please bring any earlier records and a list of current medicines on the day of your visit.</p>
  <p class="mono">Our clinic staff will guide you through each step and answer any questions you may have about tests, results or follow up care.</p>
  <p class="mono">Should your plans change, kindly let our front desk know at least one day ahead so we can offer the time to another patient.</p>
  <p class="mono">Thank you for choosing our medical services.</p>
  <div class="signoff"><div class="sig-line"></div>Your Name<br><small>Designation</small></div>
  <div class="lh-contact">
    <ul class="contact">
      <li>Phone : (+012) 555 014 2</li>
      <li>Email : info@brindlewoodmedical.com</li>
      <li>Web : www.brindlewoodmedical.com</li>
      <li>Address : 18 Harrow Lane, Millbrook, NJ 07999</li>
    </ul>
  </div>
  <div class="accent"></div>
</section>

<!-- Business card -->
<section class="item card-front">
  <div class="brand"><span class="mark"></span>brindlewood</div>
  <div class="card-name">your name<small>designation</small></div>
  <ul class="contact">
    <li>Phone : (+012) 555 014 2</li>
    <li>Email : info@brindlewoodmedical.com</li>
    <li>Web : www.brindlewoodmedical.com</li>
    <li>Address : 18 Harrow Lane, Millbrook, NJ 07999</li>
  </ul>
  <div class="accent"></div>
</section>
<section class="item card-back pattern" role="img" aria-label="Card back with hexagon pattern">
  <div class="brand light"><span class="mark"></span>brindlewood</div>
</section>

<!-- Fax cover sheet -->
<section class="item sheet fax">
  <div class="brand"><span class="mark"></span>brindlewood medical services</div>
  <div class="sheet-title">FAX COVER SHEET</div>
  <div class="fax-fields">
    <span>To : &nbsp;{ Recipient Name }</span><span>From : { Recipient Name }</span>
    <span>Fax : { Recipient Name }</span><span>Fax : &nbsp;{ Recipient Name }</span>
    <span>Phone : { Recipient Name }</span><span>Phone : { Recipient Name }</span>
    <span>Date : { Recipient Name }</span><span># Of Pages : { Recipient Name }</span>
    <span>Subject : { Recipient Name }</span><span></span>
  </div>
  <div class="fax-rule"></div>
  <div class="fax-body">
    <p class="mono">(Message To Sender)</p><br>
    <p class="mono">Please find the attached patient referral forms and lab results requested by your office earlier this week.</p><br>
    <p class="mono">Kindly review the pages and confirm receipt by phone or fax at your earliest convenience.</p><br>
    <p class="mono">All documents are confidential and intended only for the named recipient.</p>
  </div>
  <div class="accent"></div>
</section>

<!-- Invoice -->
<section class="item sheet invoice">
  <div class="brand"><span class="mark"></span>brindlewood</div>
  <div class="sheet-title">INVOICE</div>
  <div class="inv-head">
    <ul class="contact" style="color:#666;font-size:2.8px">
      <li>Phone : (+012) 555 014 2</li>
      <li>Email : info@brindlewoodmedical.com</li>
      <li>Web : www.brindlewoodmedical.com</li>
      <li>Address : 18 Harrow Lane, Millbrook, NJ 07999</li>
    </ul>
    <div class="mono" style="text-align:right;font-size:3px">INVOICE # 12345<br>DATE : 10/05/2025</div>
  </div>
  <table class="inv-table">
    <thead><tr><th>QTY</th><th>PRODUCT DESCRIPTION</th><th class="num">PRICE</th><th class="num">TOTAL</th></tr></thead>
    <tbody>
      <tr><td>1</td><td>PROJECT Title 1</td><td class="num">$ 50.00</td><td class="num">$250.00</td></tr>
      <tr><td>2</td><td>PROJECT Title 2</td><td class="num">$ 50.00</td><td class="num">$250.00</td></tr>
      <tr><td>3</td><td>PROJECT Title 3</td><td class="num">$ 50.00</td><td class="num">$250.00</td></tr>
      <tr><td>4</td><td>PROJECT Title 4</td><td class="num">$ 50.00</td><td class="num">$250.00</td></tr>
      <tr><td>5</td><td>PROJECT Title 5</td><td class="num">$ 50.00</td><td class="num">$250.00</td></tr>
    </tbody>
  </table>
  <div class="inv-notes mono" style="font-size:2.8px">Bank :<br>Account Name :<br>Account Number :<br>Payment Method :</div>
  <div class="inv-totals mono" style="font-size:3px">Subtotal &nbsp; $4,250.00<br>Tax Rate &nbsp; 0.00%</div>
  <div class="inv-total">TOTAL &nbsp;&nbsp; $415.00</div>
  <div class="inv-thanks mono" style="font-size:3px">THANK YOU FOR YOUR BUSINESS<br>Payment is due within 30 days of invoice date.</div>
  <div class="inv-sign"></div>
  <div class="accent"></div>
</section>

<!-- ID badge front -->
<section class="item badge badge-front">
  <span class="slot"></span>
  <div class="badge-photo" role="img" aria-label="Staff portrait photo"></div>
  <div class="badge-name">YOUR NAME<small>Designation</small></div>
  <div class="brand"><span class="mark"></span>brindlewood</div>
  <div class="accent"></div>
</section>

<!-- ID badge back -->
<section class="item badge badge-back">
  <span class="slot"></span>
  <div class="badge-info">
    <span>Employee Code</span><span>:</span><span>BMS2047165</span>
    <span>Office Address</span><span>:</span><span>18 Harrow Lane,<br>Millbrook,<br>NJ 07999</span>
    <span>Contact No</span><span>:</span><span>(+012) 555 014 2</span>
    <span>Blood Group</span><span>:</span><span>A+</span>
  </div>
  <div class="brand"><span class="mark"></span>brindlewood</div>
  <div class="badge-url">www.brindlewoodmedical.com</div>
  <div class="accent"></div>
</section>

<!-- Thank you card -->
<section class="item thanks">
  <div class="thanks-word w1">Thank</div>
  <div class="stetho" role="img" aria-label="Stethoscope illustration forming the letter Y"></div>
  <div class="thanks-word w2">ou</div>
  <p class="thanks-copy">Thank you so much for your Support of<br>Our Medical Services</p>
  <div class="brand"><span class="mark"></span>brindlewood</div>
  <div class="accent"></div>
</section>

<!-- Envelope back -->
<section class="item env-back">
  <div class="env-flap pattern" role="img" aria-label="Envelope flap with hexagon pattern"></div>
  <div class="brand light"><span class="mark"></span>brindlewood medical services</div>
</section>

<!-- Envelope front -->
<section class="item env-front">
  <div class="brand"><span class="mark"></span>brindlewood</div>
  <div class="env-contact">
    <ul class="contact">
      <li>Phone : (+012) 555 014 2</li>
      <li>Email : info@brindlewoodmedical.com</li>
      <li>Web address : www.brindlewoodmedical.com</li>
      <li>Address : 18 Harrow Lane, Millbrook, NJ 07999</li>
    </ul>
  </div>
  <div class="env-window"></div>
</section>

<!-- Stamp impression -->
<section class="item stamp">
  <div class="brand"><span class="mark"></span>brindlewood</div>
</section>

<!-- Notebook -->
<section class="item notebook pattern" role="img" aria-label="Notebook cover with hexagon pattern">
  <div class="brand light"><span class="mark"></span>brindlewood</div>
  <ul class="contact notebook-contact">
    <li>Phone : (+012) 555 014 2</li>
    <li>Email : info@brindlewoodmedical.com</li>
    <li>Web : www.brindlewoodmedical.com</li>
    <li>Address : 18 Harrow Lane, Millbrook, NJ 07999</li>
  </ul>
</section>
<div class="rings">
  <span></span><span></span><span></span><span></span><span></span><span></span><span></span><span></span>
  <span></span><span></span><span></span><span></span><span></span><span></span>
</div>

</body>
</html>
```